Luxury Business Card Design for High-End Window Treatments

Gilded Vantages
Custom Plantation Shutters & Architectural Shading Systems

⸻

BACK

Daniel Forsythe
Owner

Custom Interior & Exterior Window Treatments

919-482-7034
gildedvantages.com

I have included a picture that I’m hoping we can use on the back, but I’m also wondering if you can get rid of the ladder? Should we get rid of shutters , shades and blinds underneath Gilded Vantages?

Target Market(s)

High-end residential homeowners, custom home builders, architects, interior designers, and luxury renovation clients seeking premium plantation shutters and motorized architectural shading systems.

Industry/Entity Type

Custom Window treatments

Contact Information for Business Card

Front Gilded Vantages Custom Plantation Shutters Motorized Architectural Shading Systems BACK Daniel Forsythe Owner 919-482-7034 GildedVantages.com Custom Interior & Exterior Window Treatments By Appointment

Requirements
Nice to have
• Not 100% sure on nice to halves or the color but you can definitely check out my website to get a better understanding of what I’m trying to do

```html
<!DOCTYPE html>
<html lang="en">
<head>
<meta charset="utf-8">
<title>Gilded Vantages – Business Card</title>
<link href="https://fonts.googleapis.com/css2?family=Lora:wght@400;600;700&family=Lato:wght@400;700;900&display=swap" rel="stylesheet">
<style>
  :root {
    --backdrop: #2b2a2a;
    --card: #0d0d0d;
    --ink: #f2f0ec;
    --ink-soft: #d8d5cf;
    --gold: #e9c455;
    --gold-line: #b8912f;
    --label-bg: #ffffff;
    --label-ink: #1a1a1a;
  }
  * { margin: 0; padding: 0; box-sizing: border-box; }
  html, body {
    width: 1200px; height: 939px; overflow: hidden;
    background: var(--backdrop);
  }
  .canvas {
    position: relative; width: 1200px; height: 939px;
  }
  .card {
    position: absolute; left: 290px;
    width: 620px; height: 354px;
    background: var(--card);
    border-radius: 22px;
    overflow: hidden;
    box-shadow: 0 14px 30px rgba(0,0,0,.45);
  }
  .card--front { top: 62px; }
  .card--back { top: 506px; }

  /* Front */
  .front-brand {
    position: absolute; left: 0; right: 0; top: 92px;
    text-align: center;
    font-family: "Lora", serif; font-weight: 400;
    font-size: 50px; line-height: 54px;
    color: var(--ink);
  }
  .front-offer {
    position: absolute; left: 0; right: 0; top: 212px;
    text-align: center;
    font-family: "Lato", sans-serif; font-weight: 700;
    font-size: 22px; color: var(--gold);
    word-spacing: 14px;
  }
  .front-tagline {
    position: absolute; left: 0; right: 0; bottom: 36px;
    text-align: center;
    font-family: "Lora", serif; font-size: 14px;
    color: var(--ink-soft); letter-spacing: .3px;
  }

  /* Back */
  .back-brand {
    position: absolute; left: 60px; top: 60px; width: 210px;
    text-align: center;
    font-family: "Lora", serif; font-weight: 400;
    font-size: 36px; line-height: 40px;
    color: var(--ink);
  }
  .back-divider {
    position: absolute; left: 292px; top: 46px;
    width: 1.5px; height: 100px; background: var(--gold-line);
  }
  .contact {
    position: absolute; left: 318px; top: 44px;
    font-family: "Lato", sans-serif; color: var(--ink);
  }
  .contact__name {
    font-family: "Lora", serif; font-weight: 700; font-size: 25px;
    line-height: 30px;
  }
  .contact__role { font-size: 13px; color: var(--ink-soft); margin: 2px 0 8px 4px; }
  .contact__row {
    display: flex; align-items: center; gap: 8px;
    font-size: 14px; margin: 4px 0 0 8px; color: var(--ink-soft);
  }
  .contact__row svg { width: 12px; height: 12px; }
  .back-heading {
    position: absolute; left: 0; right: 0; top: 172px;
    text-align: center;
    font-family: "Lora", serif; font-weight: 600;
    font-size: 17px; letter-spacing: 2.2px;
    color: var(--gold); text-transform: uppercase;
  }
  .tiles {
    position: absolute; left: 40px; top: 208px;
    display: flex; gap: 10px;
  }
  .tile { width: 100px; height: 128px; background: var(--label-bg); display: flex; flex-direction: column; }
  .tile__photo { height: 104px; }
  .tile__label {
    flex: 1; display: flex; align-items: center; justify-content: center;
    font-family: "Lato", sans-serif; font-weight: 900;
    font-size: 10px; letter-spacing: 1.4px; color: var(--label-ink);
  }
  .photo--shutters { background: linear-gradient(160deg, #f4efe6 0%, #d9cbb3 60%, #b58a56 100%); }
  .photo--blinds { background: linear-gradient(180deg, #d6d0c8 0%, #eeebe6 55%, #c9c2b2 100%); }
  .photo--shades { background: linear-gradient(170deg, #3b4044 0%, #5f6468 55%, #8a6a4a 100%); }
  .photo--drapes { background: linear-gradient(90deg, #5d5f66 0%, #f3f3f3 35%, #ffffff 60%, #5d5f66 100%); }
  .photo--exterior { background: linear-gradient(180deg, #5f8fd6 0%, #9bb7d9 35%, #6e6d6a 65%, #7b8a5a 100%); }
</style>
</head>
<body>
<main class="canvas">

  <section class="card card--front" aria-label="Card front">
    <div class="front-brand">Gilded<br>Vantages</div>
    <div class="front-offer">Shutters Shades Blinds</div>
    <p class="front-tagline">Custom Plantation Shutters &amp; Motorized Architectural Shading Systems</p>
  </section>

  <section class="card card--back" aria-label="Card back">
    <div class="back-brand">Gilded<br>Vantages</div>
    <div class="back-divider"></div>
    <div class="contact">
      <div class="contact__name">Daniel Forsythe</div>
      <div class="contact__role">Owner</div>
      <div class="contact__row">
        <svg viewBox="0 0 24 24" aria-hidden="true"><path fill="#d8d5cf" d="M6.6 10.8a15.1 15.1 0 0 0 6.6 6.6l2.2-2.2a1 1 0 0 1 1-.25 11.4 11.4 0 0 0 3.6.57 1 1 0 0 1 1 1V20a1 1 0 0 1-1 1A17 17 0 0 1 3 4a1 1 0 0 1 1-1h3.5a1 1 0 0 1 1 1c0 1.25.2 2.45.57 3.57a1 1 0 0 1-.25 1z"/></svg>
        <span>919-482-7034</span>
      </div>
      <div class="contact__row">
        <svg viewBox="0 0 24 24" aria-hidden="true"><g fill="none" stroke="#d8d5cf" stroke-width="2"><circle cx="12" cy="12" r="10"/><path d="M2 12h20M12 2c3 3 3 17 0 20M12 2c-3 3-3 17 0 20"/></g></svg>
        <span>gildedvantages.com</span>
      </div>
    </div>
    <h2 class="back-heading">Custom Interior &amp; Exterior Window Treatments</h2>
    <div class="tiles">
      <figure class="tile"><div class="tile__photo photo--shutters" role="img" aria-label="Living room with arched windows fitted with white plantation shutters"></div><figcaption class="tile__label">SHUTTERS</figcaption></figure>
      <figure class="tile"><div class="tile__photo photo--blinds" role="img" aria-label="Bright room with light horizontal blinds over a window"></div><figcaption class="tile__label">BLINDS</figcaption></figure>
      <figure class="tile"><div class="tile__photo photo--shades" role="img" aria-label="Study with dark roman shades above a wooden desk"></div><figcaption class="tile__label">SHADES</figcaption></figure>
      <figure class="tile"><div class="tile__photo photo--drapes" role="img" aria-label="Tall window framed by grey drapes and sheer curtains"></div><figcaption class="tile__label">DRAPES</figcaption></figure>
      <figure class="tile"><div class="tile__photo photo--exterior" role="img" aria-label="House with a screened exterior porch under blue sky"></div><figcaption class="tile__label">EXTERIOR</figcaption></figure>
    </div>
  </section>

</main>
</body>
</html>
```